Redesign website

I purchased a business a few months ago and I'm in the process on rebranding everything and creating a new website. I want the new website completely different with 5 pages and nice pictures on every page. Also I want my new logo and colors to included on the site.
Current Site https://www.brindlehoundco.com

Industry/Entity Type

Dog Sitting

Coding

Coded - Design and coding required

Number of Pages Required

5+ page

Requirements
Must have
• I have pictures and a video I can shared to use for the website.
Just as the current site it should have an option to be taken to the site I have to make reservations.
Nice to have
• Would be nice to have social media intergrations

```html
<!DOCTYPE html>
<html lang="en">
<head>
<meta charset="utf-8">
<title>About Us – Brindle Hound</title>
<link href="https://fonts.googleapis.com/css2?family=Montserrat:wght@300;400;500&family=Open+Sans:wght@400;600;700&display=swap" rel="stylesheet">
<style>
:root{
  --magenta:#c4128c;
  --pink:#d4198f;
  --teal:#19b4cc;
  --sky:#16a9e0;
  --ink:#222;
  --muted:#9a9a9a;
  --light:#f5f5f5;
  --hero:#ebebeb;
  --white:#fff;
}
*{margin:0;padding:0;box-sizing:border-box}
html,body{width:1200px;height:2581px;overflow:hidden}
body{position:relative;background:var(--white);font-family:"Open Sans",sans-serif;color:var(--ink)}
.abs{position:absolute}
.head{font-family:"Montserrat",sans-serif;font-weight:300;color:var(--ink)}
.accent{color:var(--pink)}
.muted{color:var(--muted);font-size:13px;line-height:21px}
a{color:inherit;text-decoration:none}

.topbar{left:0;top:0;width:1200px;height:39px;background:var(--magenta);color:#fff;font-size:11px}
.social-mini{display:flex;gap:14px;font-size:10px;font-weight:700;letter-spacing:.3px}
.topbar .social-mini{left:160px;top:13px}
.contact-top{right:163px;top:12px;display:flex;gap:14px;align-items:center}
.contact-top span{display:flex;align-items:center;gap:8px}

.nav{left:0;top:39px;width:1200px;height:67px;background:#fff}
.brand{display:flex;align-items:center;gap:6px;font-family:"Montserrat",sans-serif;font-weight:500;font-size:15px;color:var(--pink)}
.brand i{width:14px;height:14px;border-radius:50%;background:var(--teal);display:block}
.nav .brand{left:160px;top:24px}
.menu{right:164px;top:27px;display:flex;gap:30px;font-size:11px;color:#333}

.hero{left:0;top:106px;width:1200px;height:225px;background:var(--hero);overflow:hidden}
.hero h1{position:absolute;left:0;width:1200px;top:96px;text-align:center;font-size:36px}
.hero-photo{left:880px;top:6px;width:270px;height:219px;border-radius:120px 120px 0 0;background:radial-gradient(circle at 50% 40%,#f3e2c6,#dcc29a 55%,#e9e6e4)}
.ring{border:1px solid #dcdcdc;border-radius:50%}
.dot{background:#dcdcdc;border-radius:50%}
.strip{left:0;top:331px;width:1200px;height:20px;background:var(--light)}
.crumb{left:375px;top:315px;width:448px;height:36px;background:#fff;border-radius:24px 24px 0 0;text-align:center;font-size:11px;padding-top:11px}
.crumb b{font-weight:600;color:#333}.crumb span{color:var(--muted)}

.care h2{left:160px;top:448px;font-size:28px}
.care p{left:160px;top:490px;width:355px}
.feat{top:630px;width:90px;font-family:"Montserrat",sans-serif;font-size:14px;line-height:17px;color:#333}
.feat svg{display:block;margin-bottom:12px}
.video{left:610px;top:455px;width:427px;height:247px;background:linear-gradient(100deg,#7a5a35 0%,#6d8a3f 30%,#8aa84a 60%,#3f7c8a 100%)}
.play{left:802px;top:556px}

.services{left:0;top:756px;width:1200px;height:549px;background:var(--light)}
.center{left:0;width:1200px;text-align:center}
.services h2{top:94px;font-size:30px}
.services .sub{top:140px}
.card{top:198px;width:272px;text-align:center}
.card .pic{height:180px}
.card h3{font-family:"Montserrat",sans-serif;font-weight:400;font-size:20px;margin-top:18px}
.card p{font-size:13px;line-height:17px;margin:6px 8px 0}
.card a{display:block;margin-top:12px;font-size:12px;font-weight:700}

.team h2{left:160px;top:1400px;font-size:30px}
.team p.intro{left:160px;top:1443px}
.member{width:430px;height:202px}
.member .photo{position:absolute;left:0;top:0;width:202px;height:202px;background:linear-gradient(180deg,#ebebeb 0%,#e6e3e1 60%,#7fb3c8 100%)}
.member .info{position:absolute;left:223px;top:0;width:200px}
.member h4{font-family:"Montserrat",sans-serif;font-weight:400;font-size:19px;margin-top:-2px}
.member .role{font-family:"Montserrat",sans-serif;font-size:14px;color:var(--pink);margin-top:6px}
.member .bio{font-size:12px;line-height:15px;color:var(--muted);margin-top:10px;width:175px}
.member .line{display:flex;align-items:center;gap:8px;font-size:12px;color:#333;margin-top:13px}
.member .social-mini{color:#999;margin-top:13px;gap:22px}

.news{left:0;top:2041px;width:1200px;height:304px;background:var(--light)}
.news h2{top:100px;font-size:30px}
.news .sub{top:142px;left:395px;width:410px}
.form{left:385px;top:205px;width:427px;height:36px;background:#fff;border:1px solid #e6e6e6;border-radius:18px;font-size:10px;color:#aaa;padding:11px 20px}
.form .btn{position:absolute;right:-1px;top:-1px;width:98px;height:36px;border-radius:18px;background:var(--sky);color:#fff;font-size:13px;font-weight:600;text-align:center;line-height:36px}

.footer .brand{left:160px;top:2398px}
.footer p{left:160px;top:2440px;width:195px}
.ftitle{font-family:"Montserrat",sans-serif;font-size:14px;color:#333}
.flinks{display:grid;grid-template-columns:108px 80px;row-gap:3px;font-size:12px;color:#333}
.tags{display:flex;flex-wrap:wrap;gap:8px 7px;width:190px}
.tags span{background:var(--teal);color:#fff;font-size:8px;font-weight:700;padding:4px 8px;border-radius:9px}
.finput{left:841px;top:2427px;width:200px;height:35px;border:1px solid #e6e6e6;border-radius:18px;font-size:10px;color:#aaa;padding:10px 20px}
.finput i{position:absolute;right:2px;top:2px;width:30px;height:30px;border-radius:50%;background:var(--sky);display:flex;align-items:center;justify-content:center}

.bottombar{left:0;top:2533px;width:1200px;height:48px;background:var(--teal);color:#fff;font-size:11px}
.bottombar .copy{left:160px;top:17px}
.bottombar .social-mini{right:163px;top:17px}
</style>
</head>
<body>

<header class="abs topbar">
  <div class="abs social-mini"><span>Fb</span><span>Tw</span><span>Ig</span></div>
  <div class="abs contact-top">
    <span><svg width="13" height="13" viewBox="0 0 24 24"><path fill="#fff" d="M6.6 10.8a15 15 0 0 0 6.6 6.6l2.2-2.2c.3-.3.7-.4 1-.2 1.1.4 2.3.6 3.6.6.6 0 1 .4 1 1V20c0 .6-.4 1-1 1C10.6 21 3 13.4 3 4c0-.6.4-1 1-1h3.5c.6 0 1 .4 1 1 0 1.3.2 2.5.6 3.6.1.3 0 .7-.2 1z"/></svg>+1 123 456 789</span>
    <span><svg width="13" height="11" viewBox="0 0 13 11"><rect x=".5" y=".5" width="12" height="10" fill="none" stroke="#fff"/><path d="M.5 .5l6 5 6-5" fill="none" stroke="#fff"/></svg>info@example.com</span>
  </div>
</header>

<nav class="abs nav">
  <div class="abs brand"><i></i>Brindle Hound</div>
  <div class="abs menu"><a>Home</a><a>About Us</a><a>Services &#9662;</a><a>Gallery</a><a>Blog</a><a>Contact Us</a></div>
</nav>

<section class="abs hero">
  <div class="abs ring" style="left:170px;top:-30px;width:80px;height:80px"></div>
  <div class="abs ring" style="left:-90px;top:130px;width:180px;height:180px"></div>
  <div class="abs ring" style="left:774px;top:22px;width:78px;height:78px"></div>
  <div class="abs ring" style="left:1145px;top:-50px;width:100px;height:100px"></div>
  <div class="abs dot" style="left:81px;top:34px;width:11px;height:11px"></div>
  <div class="abs dot" style="left:245px;top:160px;width:11px;height:11px"></div>
  <div class="abs dot" style="left:535px;top:46px;width:11px;height:11px"></div>
  <div class="abs dot" style="left:326px;top:0;width:8px;height:8px"></div>
  <h1 class="head">About Us</h1>
  <div class="abs hero-photo" role="img" aria-label="Labrador puppy wearing a stethoscope"></div>
</section>
<div class="abs strip"></div>
<div class="abs crumb"><b>Home</b> &rsaquo; <span>About Us</span></div>

<section class="care">
  <h2 class="abs head">Daily <span class="accent">Dog</span> Care</h2>
  <p class="abs muted">Lorem ipsum dolor sit amet, consectetur adipiscing elit. Donec viverra laoreet gravida. Donec sit amet nisi id nulla efficitur volutpat. Maecenas ac tellus et arcu egestas molestie at ut diam. Aenean sagittis, urna in iaculis feugiat, turpis nisi fringilla odio, eu tempor tortor augue sed elit.</p>
  <div class="abs feat" style="left:160px">
    <svg width="32" height="32" viewBox="0 0 32 32" fill="none" stroke="#19b4cc" stroke-width="1.6"><circle cx="16" cy="16" r="6"/><path d="M16 2v5M16 25v5M2 16h5M25 16h5M6 6l3.5 3.5M22.5 22.5L26 26M6 26l3.5-3.5M22.5 9.5L26 6"/></svg>
    Daily<br>Walking</div>
  <div class="abs feat" style="left:279px">
    <svg width="32" height="32" viewBox="0 0 32 32" fill="none" stroke="#19b4cc" stroke-width="1.6"><ellipse cx="9" cy="12" rx="2.5" ry="3.5"/><ellipse cx="14" cy="7" rx="2.5" ry="3.5"/><ellipse cx="20" cy="7" rx="2.5" ry="3.5"/><ellipse cx="25" cy="12" rx="2.5" ry="3.5"/><path d="M17 15c-5 0-9 8-6 10 2 1 4-1 6-1s4 2 6 1c3-2-1-10-6-10z"/></svg>
    Regular<br>Feeding</div>
  <div class="abs feat" style="left:390px">
    <svg width="34" height="34" viewBox="0 0 34 34" fill="none" stroke="#19b4cc" stroke-width="1.6"><circle cx="17" cy="18" r="11"/><path d="M17 11v7l5 3M4 8l5-5M30 8l-5-5M9 30l-2 3M25 30l2 3"/></svg>
    Saving<br>Your Time</div>
  <div class="abs video" role="img" aria-label="Video still of a small white dog sitting on grass"></div>
  <svg class="abs play" width="46" height="46" viewBox="0 0 46 46" fill="none" stroke="#fff" stroke-width="2.5"><circle cx="23" cy="23" r="21"/><path d="M18 14l13 9-13 9z"/></svg>
</section>

<section class="abs services">
  <h2 class="abs center head">Lorem ipsum <span class="accent">dolor sit amet</span>, consectetur</h2>
  <p class="abs center muted sub">We provide high-quality dog care services and advice for a well-trained dog</p>
  <div class="abs card" style="left:160px">
    <div class="pic" role="img" aria-label="Yorkshire terrier standing on green grass" style="background:linear-gradient(160deg,#a9c64a,#6f9a2a)"></div>
    <h3>Training And Socialization</h3>
    <p class="muted">Training and socializing your dog will ensure their confident and happy adulthood.</p>
    <a>Read More</a></div>
  <div class="abs card" style="left:463px">
    <div class="pic" role="img" aria-label="Fluffy golden doodle walking on a lawn" style="background:linear-gradient(180deg,#7b5b3c 0%,#a88b6a 35%,#6f8d3a 100%)"></div>
    <h3>Breeds</h3>
    <p class="muted">Discover more facts and information about different Labrador Retriever breeds.</p>
    <a>Read More</a></div>
  <div class="abs card" style="left:765px">
    <div class="pic" role="img" aria-label="Labrador retriever lying in a meadow" style="background:linear-gradient(180deg,#3f6a2b 0%,#8aa64a 50%,#d9b97a 75%,#7f9a3c 100%)"></div>
    <h3>Dog Health</h3>
    <p class="muted">Detailed information about vaccinations, diseases, and other health-related topics.</p>
    <a>Read More</a></div>
</section>

<section class="team">
  <h2 class="abs head">Our Wonderful Team</h2>
  <p class="abs muted intro">Lorem ipsum dolor sit amet, consectetur adipiscing elit.<br>Nullam sollicitudin facilisis neque luctus lobortis.</p>

  <div class="abs member" style="left:160px;top:1524px">
    <div class="photo" role="img" aria-label="Portrait of team member"></div>
    <div class="info"><h4>Clara Whitfield</h4><div class="role">Founder, Director</div>
      <div class="bio">Duis aute irure dolor in reprehenderit in voluptate velit esse cillum.</div>
      <div class="line"><svg width="13" height="13" viewBox="0 0 24 24"><path fill="#19b4cc" d="M6.6 10.8a15 15 0 0 0 6.6 6.6l2.2-2.2c.3-.3.7-.4 1-.2 1.1.4 2.3.6 3.6.6.6 0 1 .4 1 1V20c0 .6-.4 1-1 1C10.6 21 3 13.4 3 4c0-.6.4-1 1-1h3.5c.6 0 1 .4 1 1 0 1.3.2 2.5.6 3.6.1.3 0 .7-.2 1z"/></svg>+1 23-456-7890</div>
      <div class="line"><svg width="13" height="10" viewBox="0 0 13 10"><rect width="13" height="10" fill="#19b4cc"/><path d="M0 0l6.5 5L13 0" fill="none" stroke="#fff"/></svg>info@example.com</div>
      <div class="social-mini"><span>Fb</span><span>Tw</span><span>Ig</span></div></div>
  </div>
  <div class="abs member" style="left:614px;top:1524px">
    <div class="photo" role="img" aria-label="Portrait of team member"></div>
    <div class="info"><h4>Clara Whitfield</h4><div class="role">Founder, Director</div>
      <div class="bio">Duis aute irure dolor in reprehenderit in voluptate velit esse cillum.</div>
      <div class="line"><svg width="13" height="13" viewBox="0 0 24 24"><path fill="#19b4cc" d="M6.6 10.8a15 15 0 0 0 6.6 6.6l2.2-2.2c.3-.3.7-.4 1-.2 1.1.4 2.3.6 3.6.6.6 0 1 .4 1 1V20c0 .6-.4 1-1 1C10.6 21 3 13.4 3 4c0-.6.4-1 1-1h3.5c.6 0 1 .4 1 1 0 1.3.2 2.5.6 3.6.1.3 0 .7-.2 1z"/></svg>+1 23-456-7890</div>
      <div class="line"><svg width="13" height="10" viewBox="0 0 13 10"><rect width="13" height="10" fill="#19b4cc"/><path d="M0 0l6.5 5L13 0" fill="none" stroke="#fff"/></svg>info@example.com</div>
      <div class="social-mini"><span>Fb</span><span>Tw</span><span>Ig</span></div></div>
  </div>
  <div class="abs member" style="left:160px;top:1764px">
    <div class="photo" role="img" aria-label="Portrait of team member"></div>
    <div class="info"><h4>Clara Whitfield</h4><div class="role">Founder, Director</div>
      <div class="bio">Duis aute irure dolor in reprehenderit in voluptate velit esse cillum.</div>
      <div class="line"><svg width="13" height="13" viewBox="0 0 24 24"><path fill="#19b4cc" d="M6.6 10.8a15 15 0 0 0 6.6 6.6l2.2-2.2c.3-.3.7-.4 1-.2 1.1.4 2.3.6 3.6.6.6 0 1 .4 1 1V20c0 .6-.4 1-1 1C10.6 21 3 13.4 3 4c0-.6.4-1 1-1h3.5c.6 0 1 .4 1 1 0 1.3.2 2.5.6 3.6.1.3 0 .7-.2 1z"/></svg>+1 23-456-7890</div>
      <div class="line"><svg width="13" height="10" viewBox="0 0 13 10"><rect width="13" height="10" fill="#19b4cc"/><path d="M0 0l6.5 5L13 0" fill="none" stroke="#fff"/></svg>info@example.com</div>
      <div class="social-mini"><span>Fb</span><span>Tw</span><span>Ig</span></div></div>
  </div>
  <div class="abs member" style="left:614px;top:1764px">
    <div class="photo" role="img" aria-label="Portrait of team member"></div>
    <div class="info"><h4>Clara Whitfield</h4><div class="role">Founder, Director</div>
      <div class="bio">Duis aute irure dolor in reprehenderit in voluptate velit esse cillum.</div>
      <div class="line"><svg width="13" height="13" viewBox="0 0 24 24"><path fill="#19b4cc" d="M6.6 10.8a15 15 0 0 0 6.6 6.6l2.2-2.2c.3-.3.7-.4 1-.2 1.1.4 2.3.6 3.6.6.6 0 1 .4 1 1V20c0 .6-.4 1-1 1C10.6 21 3 13.4 3 4c0-.6.4-1 1-1h3.5c.6 0 1 .4 1 1 0 1.3.2 2.5.6 3.6.1.3 0 .7-.2 1z"/></svg>+1 23-456-7890</div>
      <div class="line"><svg width="13" height="10" viewBox="0 0 13 10"><rect width="13" height="10" fill="#19b4cc"/><path d="M0 0l6.5 5L13 0" fill="none" stroke="#fff"/></svg>info@example.com</div>
      <div class="social-mini"><span>Fb</span><span>Tw</span><span>Ig</span></div></div>
  </div>
</section>

<section class="abs news">
  <h2 class="abs center head">Get The Latest News</h2>
  <p class="abs muted sub" style="text-align:center">Receive a 10% discount code via email when you sign up for our news &amp; updates.</p>
  <div class="abs form">E-Mail<span class="btn">Subscribe</span></div>
</section>

<footer class="footer">
  <div class="abs brand"><i></i>Brindle Hound</div>
  <p class="abs muted">Lorem ipsum dolor sit amet, consectetur adipiscing elit. Donec viverra laoreet gravida.</p>
  <div class="abs ftitle" style="left:388px;top:2393px">Categories</div>
  <div class="abs flinks" style="left:388px;top:2424px"><a>Home</a><a>Gallery</a><a>About Us</a><a>Shop</a><a>Services</a><a>Pages</a><a>Our Team</a><a>Contacts</a></div>
  <div class="abs ftitle" style="left:614px;top:2393px">Tags</div>
  <div class="abs tags" style="left:614px;top:2427px"><span>NEWS</span><span>BREED</span><span>LABRADOR</span><span>PUPPIES</span><span>SHOP</span><span>TRAINING</span><span>CHAMPIONHIP</span><span>RETRIEVER</span></div>
  <div class="abs ftitle" style="left:841px;top:2393px">Subscribe</div>
  <div class="abs finput">E-Mail<i><svg width="10" height="10" viewBox="0 0 10 10"><path d="M3 1l4 4-4 4" fill="none" stroke="#fff" stroke-width="2"/></svg></i></div>
</footer>

<div class="abs bottombar">
  <div class="abs copy">©2020 All rights reserved. Privacy Policy</div>
  <div class="abs social-mini"><span>Fb</span><span>Tw</span><span>Ig</span></div>
</div>

</body>
</html>
```